Management consultant needs business cards

We need a design for a personal/professional business card for a management consultant. Work is typically focused on the b2b space, helping companies improve their operations. The final design should communicate efficiency and helping companies and people achieve their full potential.

Company name is "Copperfen Consultants"

Brand promise is "Finding Potential - Unleashing Performance"

We come from major consulting firms (Haldorne, Vesk, TQP) but would like to project a slightly more modern feel than those players.

Target Market(s)

Targeting B2B markets such as banks or companies.

Industry/Entity Type

Business

Requirements
Must have
• The card must communicate the following information:

Nolan J Brackett
Managing Director
Copperfen Consultants
Phone: 416-555-0172
nolan.brackett@copperfenconsultants.example
www.copperfenconsultants.example

214 Pellworth Ave
Toronto, ON M5X 9Z7

Back side should have
"Finding Potential - Unleashing Performance"

```html
<!DOCTYPE html>
<html lang="en">
<head>
<meta charset="utf-8">
<title>Copperfen Consultants – Business Card</title>
<link rel="stylesheet" href="https://fonts.googleapis.com/css2?family=Roboto:wght@300;400;500&display=swap">
<style>
  :root {
    --card-white: #ffffff;
    --band-grey: #c9c9c9;
    --rule-dark: #2e2e2e;
    --ink: #333333;
    --logo-ink: #4a4a4a;
  }
  * { margin: 0; padding: 0; box-sizing: border-box; }
  html, body {
    width: 1200px;
    height: 686px;
    overflow: hidden;
    background: var(--card-white);
    font-family: "Roboto", Arial, sans-serif;
    color: var(--ink);
  }
  .card {
    position: relative;
    width: 1200px;
    height: 686px;
    background: var(--card-white);
  }
  .wordmark {
    position: absolute;
    left: 80px;
    top: 128px;
    color: var(--logo-ink);
    font-weight: 500;
    text-transform: uppercase;
    line-height: 1;
  }
  .wordmark__primary {
    display: block;
    font-size: 98px;
    letter-spacing: 4px;
  }
  .wordmark__secondary {
    display: block;
    margin-top: 8px;
    font-size: 52px;
    letter-spacing: 8px;
  }
  .rule-top {
    position: absolute;
    left: 0; top: 331px;
    width: 1200px; height: 12px;
    background: var(--rule-dark);
  }
  .info-band {
    position: absolute;
    left: 0; top: 343px;
    width: 1200px; height: 331px;
    background: var(--band-grey);
  }
  .rule-bottom {
    position: absolute;
    left: 0; top: 674px;
    width: 1200px; height: 12px;
    background: var(--rule-dark);
  }
  .person {
    position: absolute;
    left: 80px;
    top: 398px;
  }
  .person__name {
    font-size: 66px;
    font-weight: 400;
    line-height: 1;
  }
  .person__title {
    margin-top: 4px;
    font-size: 38px;
    font-weight: 400;
    line-height: 1;
  }
  .contact-list {
    position: absolute;
    left: 700px;
    top: 412px;
    list-style: none;
  }
  .contact-list__item {
    display: flex;
    align-items: center;
    height: 50px;
  }
  .contact-list__item--phone { height: 56px; }
  .contact-list__icon {
    width: 30px;
    height: 30px;
    margin-right: 14px;
    flex: none;
    fill: var(--ink);
  }
  .contact-list__text {
    font-size: 20px;
    font-weight: 400;
    white-space: nowrap;
  }
  .contact-list__item--phone .contact-list__text {
    font-size: 38px;
  }
</style>
</head>
<body>
  <div class="card">
    <div class="wordmark">
      <span class="wordmark__primary">Copperfen</span>
      <span class="wordmark__secondary">Consultants</span>
    </div>

    <div class="rule-top"></div>
    <div class="info-band"></div>
    <div class="rule-bottom"></div>

    <div class="person">
      <p class="person__name">Nolan J Brackett</p>
      <p class="person__title">Managing Director</p>
    </div>

    <ul class="contact-list">
      <li class="contact-list__item contact-list__item--phone">
        <svg class="contact-list__icon" viewBox="0 0 24 24" aria-hidden="true">
          <path d="M6.6 10.8c1.4 2.8 3.8 5.1 6.6 6.6l2.2-2.2c.3-.3.7-.4 1-.2 1.1.4 2.3.6 3.6.6.6 0 1 .4 1 1V20c0 .6-.4 1-1 1C10.6 21 3 13.4 3 4c0-.6.4-1 1-1h3.5c.6 0 1 .4 1 1 0 1.3.2 2.5.6 3.6.1.3 0 .7-.2 1l-2.3 2.2z"/>
        </svg>
        <span class="contact-list__text">416-555-0172</span>
      </li>
      <li class="contact-list__item">
        <svg class="contact-list__icon" viewBox="0 0 24 24" aria-hidden="true">
          <path d="M3 5h18v14H3V5zm2 2v.4l7 4.6 7-4.6V7H5zm14 2.8-7 4.6-7-4.6V17h14V9.8z"/>
        </svg>
        <span class="contact-list__text">nolan.brackett@copperfenconsultants.example</span>
      </li>
      <li class="contact-list__item">
        <svg class="contact-list__icon" viewBox="0 0 24 24" aria-hidden="true">
          <path d="M12 2a10 10 0 1 0 0 20 10 10 0 0 0 0-20zm6.9 6h-3a15 15 0 0 0-1.3-3.8A8 8 0 0 1 18.9 8zM12 4c.8 1.2 1.5 2.5 1.9 4h-3.8c.4-1.5 1.1-2.8 1.9-4zM4.3 14a8 8 0 0 1 0-4h3.4a16 16 0 0 0 0 4H4.3zm.8 2h3a15 15 0 0 0 1.3 3.8A8 8 0 0 1 5.1 16zm3-8h-3a8 8 0 0 1 4.3-3.8A15 15 0 0 0 8.1 8zM12 20c-.8-1.2-1.5-2.5-1.9-4h3.8c-.4 1.5-1.1 2.8-1.9 4zm2.3-6H9.7a14 14 0 0 1 0-4h4.6a14 14 0 0 1 0 4zm.3 5.8c.6-1.2 1-2.5 1.3-3.8h3a8 8 0 0 1-4.3 3.8zm1.7-5.8a16 16 0 0 0 0-4h3.4a8 8 0 0 1 0 4h-3.4z"/>
        </svg>
        <span class="contact-list__text">www.copperfenconsultants.example</span>
      </li>
      <li class="contact-list__item">
        <svg class="contact-list__icon" viewBox="0 0 24 24" aria-hidden="true">
          <path d="M12 2a7 7 0 0 0-7 7c0 5.2 7 13 7 13s7-7.8 7-13a7 7 0 0 0-7-7zm0 9.5A2.5 2.5 0 1 1 12 6.5a2.5 2.5 0 0 1 0 5z"/>
        </svg>
        <span class="contact-list__text">214 Pellworth Ave Toronto, ON M5X 9Z7</span>
      </li>
    </ul>
  </div>
</body>
</html>
```